Noche de Salsa

We need a poster to promote a party. It is a salsa night at La Tortuga, a fun night out to dance, be with friends and have a few drinks. It is an informal occasion. The drinks will not be expensive and the snack will be typical mexican food.
La Tortuga is a campus for 8 local non-profit organizations but it also has high quality event venues and outdoor areas.
We would like a file for print (11x17") and a digital file for social media.
Enclosed:
- File with poster contents in spanish.
- La Tortuga logo
- Picture of palm trees at La Tortuga (you don't have to include this if another graphic fits best.
- Pic of the outside of the restaurant, where the dancing will take place. The restaurante is right in fron of the beach. THIS PICTURE DOES NOT NECESSARILY NEEDS TO BE PART OF THE POSTER.
- La Tortuga Fact Sheet for context.
Target Market(s)
Men and women from 25 to 50 years old.
American and mexican citizens.
Industry/Entity Type
Non-Profit
Colors
Designer to choose colors to be used in the design.
Look and feel
Each slider illustrates characteristics of the customer's brand and the style your logo design should communicate.

```html
<!DOCTYPE html>
<html lang="es">
<head>
<meta charset="utf-8">
<title>Noche de Salsa · La Tortuga</title>
<link href="https://fonts.googleapis.com/css2?family=Bebas+Neue&family=Bowlby+One&family=Oswald:wght@300;400;500&family=Pacifico&display=swap" rel="stylesheet">
<style>
  :root{
    --sky-top:#3f3a86;
    --sky-mid:#8a73b8;
    --sky-pink:#d896b8;
    --sky-glow:#f2a253;
    --ground:#2a2936;
    --ground-deep:#34343f;
    --white:#ffffff;
    --mint:#e4f5ee;
    --teal:#4fa9ad;
    --teal-deep:#2f7f86;
    --gold:#f7c45a;
    --gold-deep:#e58a3b;
    --band:rgba(255,255,255,.22);
    --line:rgba(255,255,255,.55);
  }
  *{margin:0;padding:0;box-sizing:border-box}
  html,body{width:776px;height:1200px;overflow:hidden;background:#222}
  .poster{position:relative;width:776px;height:1200px;overflow:hidden;font-family:"Oswald",sans-serif;color:var(--white)}
  .scene{position:absolute;inset:0;
    background:linear-gradient(180deg,var(--sky-top) 0%,#5a4a9c 22%,var(--sky-mid) 40%,var(--sky-pink) 56%,var(--sky-glow) 68%,#b45a45 74%,var(--ground) 80%,var(--ground-deep) 100%)}
  .brand{position:absolute;left:30px;top:42px;display:flex;align-items:center;gap:12px}
  .brand-dot{width:18px;height:18px;border-radius:50%;background:var(--white)}
  .brand-name{font-family:"Oswald",sans-serif;font-weight:400;font-size:40px;letter-spacing:1px;color:var(--white)}
  .sky-icons{position:absolute;left:470px;top:55px}
  .title{position:absolute;left:0;top:0;width:776px;height:440px}
  .title-script{position:absolute;left:150px;top:150px;font-family:"Pacifico",cursive;font-size:92px;color:var(--mint);transform:rotate(-9deg);
    text-shadow:-1px 1px 0 var(--teal),-2px 2px 0 var(--teal),-3px 3px 0 var(--teal),-4px 4px 0 var(--teal),-5px 5px 0 var(--teal-deep),-6px 6px 0 var(--teal-deep)}
  .title-main{position:absolute;left:205px;top:250px;font-family:"Bowlby One",sans-serif;font-size:118px;letter-spacing:4px;color:var(--gold);transform:rotate(-8deg);
    text-shadow:-1px 1px 0 var(--gold-deep),-2px 2px 0 var(--teal),-3px 3px 0 var(--teal),-4px 4px 0 var(--teal),-5px 5px 0 var(--teal),-6px 6px 0 var(--teal-deep),-7px 7px 0 var(--teal-deep),-8px 8px 0 var(--teal-deep)}
  .bands{position:absolute;inset:0}
  .ticket{position:absolute;left:70px;top:550px;width:180px;height:180px;border-radius:50%;background:var(--gold);color:#2b2230;
    display:flex;flex-direction:column;align-items:center;justify-content:center;text-align:center;line-height:1.15}
  .ticket-label{font-family:"Oswald",sans-serif;font-weight:500;font-size:26px}
  .ticket-text{font-family:"Oswald",sans-serif;font-weight:300;font-size:22px}
  .glass{position:absolute;left:190px;top:568px}
  .date{position:absolute;left:505px;top:690px;font-family:"Bebas Neue",sans-serif;color:var(--white);transform:rotate(14deg);transform-origin:left top;line-height:.9}
  .date-day{font-size:66px;letter-spacing:1px}
  .date-month{font-size:36px}
  .date-year{font-size:60px;margin-left:18px}
  .venue{position:absolute;left:0;top:870px;width:776px;text-align:center}
  .venue-name{margin-top:14px;font-family:"Oswald",sans-serif;font-weight:500;font-size:25px;color:var(--gold);letter-spacing:.5px}
  .venue-line{font-family:"Oswald",sans-serif;font-weight:300;font-size:20px;line-height:27px;letter-spacing:.3px}
  .contact{position:absolute;left:0;top:1140px;width:776px;text-align:center;font-family:"Oswald",sans-serif;font-weight:300;font-size:20px;letter-spacing:.3px}
  .contact-lead{color:var(--gold)}
</style>
</head>
<body>
<main class="poster">
  <div class="scene" role="img" aria-label="Fotografía de siluetas de palmeras frente al mar al atardecer, cielo morado y rosa con el sol naranja en el horizonte"></div>

  <div class="brand">
    <span class="brand-dot"></span>
    <span class="brand-name">La Tortuga</span>
  </div>

  <svg class="sky-icons" width="300" height="270" viewBox="0 0 300 270" aria-hidden="true">
    <path d="M60 15 A125 125 0 1 0 200 230 A105 105 0 1 1 60 15 Z" fill="rgba(255,255,255,.08)" stroke="rgba(255,255,255,.4)" stroke-width="5"/>
    <path d="M245 45 l12 27 29 3 -22 19 7 29 -26 -15 -26 15 7 -29 -22 -19 29 -3 Z" fill="none" stroke="rgba(255,255,255,.4)" stroke-width="5" stroke-linejoin="round"/>
  </svg>

  <svg class="bands" width="776" height="1200" viewBox="0 0 776 1200" aria-hidden="true">
    <polygon points="0,620 300,540 300,690 0,760" fill="var(--band)"/>
    <polygon points="495,650 776,700 776,880 495,830" fill="var(--band)"/>
  </svg>

  <h1 class="title">
    <span class="title-script">Noche de</span>
    <span class="title-main">SALSA</span>
  </h1>

  <div class="ticket">
    <span class="ticket-label">ENTRADA:</span>
    <span class="ticket-text">$100 PESOS</span>
    <span class="ticket-text">INCLUYE 1 BEBIDA.</span>
  </div>
  <svg class="glass" width="90" height="90" viewBox="0 0 90 90" aria-hidden="true">
    <path d="M8 10 H70 L39 44 Z" fill="none" stroke="var(--white)" stroke-width="3" stroke-linejoin="round"/>
    <line x1="39" y1="44" x2="39" y2="78" stroke="var(--white)" stroke-width="3"/>
    <line x1="24" y1="80" x2="54" y2="80" stroke="var(--white)" stroke-width="3"/>
    <circle cx="70" cy="12" r="10" fill="none" stroke="var(--white)" stroke-width="3"/>
  </svg>

  <div class="date">
    <div class="date-day">VIERNES</div>
    <div class="date-month">14 DE NOVIEMBRE</div>
    <div class="date-year">2014</div>
  </div>

  <section class="venue">
    <svg width="52" height="72" viewBox="0 0 52 72" aria-hidden="true">
      <path d="M26 68 C26 68 4 40 4 25 A22 22 0 0 1 48 25 C48 40 26 68 26 68 Z" fill="none" stroke="var(--white)" stroke-width="3"/>
      <circle cx="26" cy="25" r="8" fill="none" stroke="var(--white)" stroke-width="3"/>
    </svg>
    <p class="venue-name">LA TORTUGA</p>
    <p class="venue-line">ACCESO COSTERO #4180</p>
    <p class="venue-line">(AL FINAL DE LA CALLE PALMAR, EN LA ANTIGUA BODEGA)</p>
    <p class="venue-line">COL. LAS ARENAS &nbsp;-&nbsp; C.P. 23090 &nbsp;-&nbsp; BAHÍA SERENA, B.C.S.</p>
  </section>

  <p class="contact"><span class="contact-lead">MÁS INFORMES</span> AL 148-3071 / INFO@LATORTUGA.ORG</p>
</main>
</body>
</html>
```